Flyer: Bright Days, Open Doors

Please create a two (2) page flyer. We welcome minor updates/ changes to the Bright Days Open Doors flyer that is attached as a word document. We are aiming for the same general look and feel as the original PDF attached (please note that we have updated the content and would like the designers to use what is listed in the word document).
We encourage you to provide multiple versions using pictures of different people we have on hand. Our team currently likes how the lady in the picture is looking in the direction of the text - we encourage designers to please flip the photo if needed to make this possible. We also give the permission to crop the photos as needed to fit the design better aesthetically. In addition, the team wondered about having a pdf file that allows the user to easily change out the graphic between different photos to reflect different communities best—not sure if that is as easy as it sounds. Please remember to include the funding statement - you can find it within both of the current documents. For more information about our project, please visit https://velmorakin.org/open-doors/

```html
<!DOCTYPE html>
<html lang="en">
<head>
<meta charset="utf-8">
<title>Bright Days, Open Doors – Flyer</title>
<link href="https://fonts.googleapis.com/css2?family=Anton&family=Poppins:wght@400;500;600;700&display=swap" rel="stylesheet">
<style>
  :root{
    --paper:#fdf8f1;
    --backdrop:#ffffff;
    --brand-red:#9b1b2a;
    --ink:#1b1b1b;
    --muted:#555555;
    --brand-teal:#4a7f8f;
    --photo-warm:#b98a6e;
    --photo-deep:#4a5a6e;
  }
  *{box-sizing:border-box;margin:0;padding:0}
  html,body{width:1200px;height:841px;overflow:hidden;background:var(--backdrop)}
  body{font-family:"Poppins",sans-serif;color:var(--ink);position:relative}
  .page{position:absolute;top:39px;width:532px;height:753px;background:var(--paper);overflow:hidden}
  .page--front{left:43px}
  .page--back{left:623px;padding:26px 28px 0 29px}

  /* front */
  .front__title{position:absolute;left:29px;top:26px;font-family:"Anton",sans-serif;font-size:50px;line-height:56px;letter-spacing:.3px;text-transform:uppercase}
  .front__subtitle{position:absolute;left:29px;top:148px;font-size:10px}
  .front__intro{position:absolute;left:29px;top:178px;width:290px;font-size:10.5px;line-height:13.6px}
  .front__photo{position:absolute;left:330px;top:0;width:202px;height:262px}
  .rule{position:absolute;left:29px;width:470px;height:1px;background:var(--brand-red)}
  .rule::after{content:"";position:absolute;right:-3px;top:-3px;width:7px;height:7px;border-radius:50%;background:var(--brand-red)}
  .rule--left::after{right:auto;left:-3px}
  .stat{position:absolute;top:290px;display:flex;gap:8px;align-items:flex-start}
  .stat--one{left:29px}
  .stat--two{left:272px}
  .stat__figure{font-size:38px;line-height:42px;font-weight:600;letter-spacing:-1px;color:var(--brand-red)}
  .stat__label{font-size:10.5px;line-height:13.4px;margin-top:2px}
  .stat__art{width:66px;height:86px;border-radius:4px;background:linear-gradient(160deg,#e9e0d6,#8a7f76)}
  .risk{position:absolute;left:29px;top:382px;font-size:10.5px;line-height:13.6px}
  .risk ul{list-style:none;font-weight:600}
  .risk li::before{content:"• "}
  .front__heading{position:absolute;left:29px;top:470px;font-size:18.5px;font-weight:600;color:var(--brand-red)}
  .protect{position:absolute;left:29px;top:497px;width:460px;list-style:none;font-size:10.5px;line-height:15.2px}
  .protect li{padding-left:8px;text-indent:-8px}
  .protect li::before{content:"• "}
  .front__closing{position:absolute;left:29px;top:689px;font-size:10.5px;font-weight:600}
  .front__cta{position:absolute;left:73px;top:714px;width:385px;height:24px;background:var(--brand-red);color:#fff;font-size:10.5px;display:flex;align-items:center;justify-content:center}

  /* back */
  .back__heading{font-size:17.5px;line-height:20px;font-weight:600;color:var(--brand-red)}
  .back p,.back li{font-size:10.2px;line-height:12.6px}
  .back__para{margin-top:4px}
  .back__para + .back__para{margin-top:10px}
  .back .rule{position:relative;left:0;width:470px;margin:10px 0 16px}
  .task{margin-top:7px}
  .task__lead{font-weight:600}
  .task ul{list-style:none}
  .task li::before{content:"• "}
  .back__steps{list-style:none;margin-top:12px}
  .back__steps li{padding-left:8px;text-indent:-8px}
  .back__steps li::before{content:"• "}
  .brand{position:absolute;left:206px;top:700px;display:flex;align-items:center;gap:6px;color:var(--brand-teal);font-size:10px;font-weight:600;text-transform:uppercase}
  .brand__mark{width:12px;height:12px;background:var(--brand-teal)}
  .back p.funding{position:absolute;left:36px;top:724px;width:940px;font-size:9.2px;line-height:12px;font-style:italic;color:var(--muted);transform:scale(.5);transform-origin:0 0}
</style>
</head>
<body>

<section class="page page--front">
  <h1 class="front__title">Bright Days<br>Open Doors..</h1>
  <p class="front__subtitle">Keep Your Heart and Body Healthy to Protect Your Brain</p>
  <p class="front__intro">Everyone slows down as they get older, both in body and mind. Big chances in memory or thinking that make it hard to get through the day are not a normal part of aging. These changes could be signs of early dementia or Alzheimer’s disease.</p>

  <svg class="front__photo" viewBox="0 0 202 262" role="img" aria-label="Photo of a smiling elder woman in a headscarf and patterned shawl, looking toward the text">
    <defs>
      <linearGradient id="photoTone" x1="0" y1="0" x2="1" y2="1">
        <stop offset="0" stop-color="var(--photo-warm)"/>
        <stop offset="1" stop-color="var(--photo-deep)"/>
      </linearGradient>
    </defs>
    <path d="M40 0 H202 V262 H60 C30 262 10 240 20 210 C30 180 10 150 12 110 C14 60 20 20 40 0Z" fill="var(--brand-red)"/>
    <path d="M60 10 C120 -5 190 5 202 20 V262 H70 C40 258 30 235 38 210 C46 185 30 150 32 110 C34 60 40 20 60 10Z" fill="url(#photoTone)"/>
  </svg>

  <div class="rule" style="top:268px"></div>

  <div class="stat stat--one">
    <svg width="64" height="62" viewBox="0 0 64 62" aria-hidden="true">
      <g fill="var(--ink)">
        <g id="person"><circle cx="6" cy="4" r="3.4"/><path d="M0 16 C0 9 12 9 12 16Z"/></g>
        <use href="#person" x="14"/><use href="#person" x="28"/>
        <use href="#person" x="0" y="21"/><use href="#person" x="14" y="21"/><use href="#person" x="28" y="21"/><use href="#person" x="42" y="21"/>
        <use href="#person" x="0" y="42"/><use href="#person" x="14" y="42"/>
      </g>
      <g fill="var(--brand-red)"><circle cx="34" cy="46" r="3.4"/><path d="M28 58 C28 51 40 51 40 58Z"/></g>
    </svg>
    <div>
      <div class="stat__figure">1 in 9</div>
      <p class="stat__label">People in the U.S. ages 65+<br>has Alzheimer’s dementia</p>
    </div>
  </div>

  <div class="stat stat--two">
    <div class="stat__art" role="img" aria-label="Line illustration of an elder in a feathered headdress"></div>
    <div>
      <div class="stat__figure">1 in 3</div>
      <p class="stat__label">American Indian People ages<br>65+ develops dementia</p>
    </div>
  </div>

  <div class="risk">
    <p>You are more at risk of developing dementia if you have:</p>
    <ul>
      <li>High blood pressure</li>
      <li>Diabetes or</li>
      <li>You smoke cigarettes</li>
    </ul>
  </div>

  <div class="rule rule--left" style="top:458px"></div>

  <h2 class="front__heading">You can protect your body, heart, and mind</h2>
  <ul class="protect">
    <li>Schedule a “wellness” visit and &nbsp;health screenings every year with your doctor, even if you feel ok</li>
    <li>Keep a healthy blood pressure</li>
    <li>Be active or walk every day</li>
    <li>Maintain a healthy weight for your body size</li>
    <li>Eat a healthier diet with more fresh vegetables, fruits, whole grains, and fish</li>
    <li>Stop smoking cigarettes or chewing tobacco</li>
    <li>Get help managing your high blood pressure, diabetes, or to lose extra weight</li>
    <li>Talk to your doctor about how you feel because your health can affect your brain and physical health</li>
    <li>If it is hard for you to get through the day because of forgetfulness or memory problems,see your doctor right away</li>
  </ul>
  <p class="front__closing">You can do these today to protect your mind and reduce the risk of slow down dementia</p>
  <div class="front__cta">Turn over for your checklist to keep your river of life flowing freely</div>
</section>

<section class="page page--back back">
  <h2 class="back__heading">The River of Life Flows Through Your Heart To<br>Protect Your Mind And Body</h2>
  <p class="back__para">Your heart health plays a big part in the health of your brain. Your heart is like the start of a flowing river. Blood vessels that take blood to and from your heart are like connected streams that flows through your body. They feed your brain with oxygen and energy.</p>
  <p class="back__para">You can do things to keep the streams freely flowing through your body, so your heart and brain stays strong and healthy.</p>
  <div class="rule"></div>

  <h2 class="back__heading">Working With Your Doctor</h2>
  <div class="task">
    <p class="task__lead">Make an appointment for a “wellness” checkup with your doctor every year</p>
    <ul>
      <li>You will get tests and screenings to make sure you are healthy</li>
      <li>They are usually free with Senior Care Plan B or the Tribal Wellness Service</li>
      <li>If you have concerns about your memory, talk to your doctor</li>
    </ul>
  </div>
  <div class="task">
    <p class="task__lead">Have your blood pressure checked and know your numbers</p>
    <ul>
      <li>Your blood pressure should be less than 120/80mmHg (120 over 80)</li>
      <li>If you do not know how to take your blood pressure, ask your doctor to show you</li>
    </ul>
  </div>
  <div class="task">
    <p class="task__lead">Have your weight checked regulary and know your number. If you need lose extra weight, ask your doctor about</p>
    <ul>
      <li>The right number of calories for your body</li>
      <li>Ideas for healthier food choices</li>
      <li>Support for losing weight</li>
    </ul>
  </div>
  <p class="task"><b class="task__lead">If you smoke cigarettes, or chew tobacco,</b> ask about medicine, couselling or help to stop</p>
  <p class="task"><b class="task__lead">If you do not have diabetes,</b> have your blood sugar level checked during your visit. Your blood sugar should be less than 100 mg/dL when you have not eaten</p>
  <p class="task"><b class="task__lead">If you do not have diabetes,</b> go to reguar doctor visits. Have your blood sugar and “A1C” levels checked. Your doctor wil tell you what your A1C level should be</p>
  <p class="task"><b class="task__lead">Talk with your doctor</b> about all the medicines and vitamins you take.Your doctor can make sure they do not cause any problems with your memory, sleep or brain function</p>
  <div class="rule rule--left"></div>

  <h2 class="back__heading">Other Steps You Can Take</h2>
  <ul class="back__steps">
    <li>Aim for 20 minutes of physical activity a day or 2 1/2 hours a week</li>
    <li>Eat less salt, sugar, red meat, and highly processed or packaged foods</li>
    <li>Read food labels to see how much salt (sodium) or fat is in your food</li>
    <li>Manage extra weight by making small changes. Losing a few pounds makes a difference</li>
    <li>Limit alcohol. No more 1 drink per day for women and 2 for men</li>
    <li>Take your medicine for blood pressure, diabetes, and other problems even if you feel good</li>
    <li>Get at least seven hours of sleep each night. Talk to your doctor if you have trouble sleeping</li>
    <li>Keep your mind active. Visit with people in your community, help plan tribal events, go to your senior center, teach your language, play cards, or start a new hobby</li>
  </ul>

  <div class="brand"><span class="brand__mark"></span>Velmora Kin Circle</div>
  <p class="funding">This product is supported by a federal public health agency as part of a financial assistance award totaling $348,711 with 100 percent funded by the agency. The contents are those of the author(s) and do not necessarily represent the official views of the funder.</p>
</section>

</body>
</html>
```